amber crest health and wellness group.

need a full website design , all information provided in word document labeled website blue print

Target Market(s)

first responders, military , people in crisis

Coding

Coded - Design and coding required

Number of Pages Required

1 page

```html
<!DOCTYPE html>
<html lang="en">
<head>
<meta charset="utf-8">
<title>Amber Crest Health &amp; Wellness Group</title>
<link href="https://fonts.googleapis.com/css2?family=Outfit:wght@300;400;500;600;700&display=swap" rel="stylesheet">
<style>
:root{
  --brand:#27598f;
  --brand-dark:#1f4c7e;
  --ink:#1d1d1f;
  --muted:#555a61;
  --line:#d9dde2;
  --white:#ffffff;
  --hero-a:#3b2c22;
  --hero-b:#8a6a4e;
}
*{box-sizing:border-box;margin:0;padding:0}
html,body{width:1200px;height:4079px;overflow:hidden}
body{position:relative;font-family:'Outfit',sans-serif;color:var(--ink);background:var(--white)}
.abs{position:absolute}
a{color:inherit;text-decoration:none}
.btn{position:absolute;display:flex;align-items:center;justify-content:center;background:var(--brand);color:var(--white);font-size:13px;font-weight:500;letter-spacing:-.2px}

/* hero */
.hero{left:0;top:0;width:1200px;height:713px;background:radial-gradient(ellipse at 50% 45%,#b08a63 0%,#6e5240 40%,#2f231b 100%)}
.brand-name{position:absolute;color:var(--white);font-weight:600;text-align:center;line-height:1.05}
.hero .brand-name{left:70px;top:50px;width:120px;font-size:15px}
.main-nav{position:absolute;left:328px;top:56px;display:flex;gap:32px;color:var(--white);font-size:12.5px;font-weight:400}
.nav-rule{left:76px;top:116px;width:1048px;height:1px;background:rgba(255,255,255,.45)}
.hero h1{position:absolute;left:0;top:216px;width:1200px;text-align:center;color:var(--white);font-size:52px;font-weight:600;letter-spacing:-1.5px}
.hero .lede{position:absolute;left:0;top:293px;width:1200px;text-align:center;color:var(--white);font-size:12.5px;letter-spacing:-.2px}
.slide-arrow{position:absolute;top:292px}
.dots{position:absolute;left:570px;top:664px;display:flex;gap:8px}
.dots span{width:12px;height:12px;border-radius:50%;border:1.5px solid var(--white)}
.dots span.on{background:var(--brand);border-color:var(--brand)}

/* about */
.eyebrow{position:absolute;color:var(--brand);font-size:15px;font-weight:600;letter-spacing:-.3px}
.section-title{position:absolute;font-size:33px;font-weight:600;letter-spacing:-.8px;line-height:1.3;color:var(--ink)}
.photo{position:absolute}
.body-copy{position:absolute;font-size:11.5px;line-height:1.65;color:var(--muted)}

/* services */
.service{position:absolute;top:1684px;width:252px;height:277px;border-bottom:2px solid var(--line)}
.service .photo{left:0;top:0;width:252px;height:225px}
.service h3{position:absolute;left:0;top:240px;width:252px;text-align:center;font-size:16px;font-weight:600;letter-spacing:-.3px}

/* video */
.video{left:0;top:2118px;width:1200px;height:472px;background:linear-gradient(100deg,#6a5445 0%,#9b7b61 35%,#4f5d70 60%,#8b6a4c 100%)}
.play{position:absolute;left:511px;top:2265px;width:178px;height:178px;border:2px solid var(--white);border-radius:50%;display:flex;align-items:center;justify-content:center;color:var(--white);font-size:15px;font-weight:500}

/* audiences */
.audience{position:absolute;top:2775px;width:320px;text-align:center}
.audience .icon{width:57px;height:57px;margin:0 auto;background:var(--brand);display:flex;align-items:center;justify-content:center}
.audience p{margin-top:22px;font-size:11.5px;color:var(--muted)}
.v-rule{position:absolute;top:2754px;width:1px;height:124px;background:var(--line)}

/* cta + footer */
.cta-band{left:0;top:3459px;width:1200px;height:620px;background:var(--brand)}
.cta-band h2{position:absolute;left:0;top:3522px;width:1200px;text-align:center;color:var(--white);font-size:52px;font-weight:600;letter-spacing:-1.5px}
.btn-light{background:var(--white);color:var(--ink)}
.btn-outline{background:transparent;border:1.5px solid var(--white)}
.foot-rule{left:76px;width:1048px;height:1px;background:rgba(255,255,255,.5)}
.footer-nav{position:absolute;left:0;top:3877px;width:1200px;display:flex;justify-content:center;gap:40px;color:var(--white);font-size:12.5px}
.social{position:absolute;top:3932px;left:512px;display:flex;gap:10px}
.social span{width:36px;height:36px;background:var(--white)}
.social span.dim{background:rgba(255,255,255,.25)}
.copyright{position:absolute;left:0;top:4043px;width:1200px;text-align:center;color:var(--white);font-size:12px}
.to-top{position:absolute;left:1141px;top:4008px;width:39px;height:39px;background:var(--white);display:flex;align-items:center;justify-content:center}
</style>
</head>
<body>

<header class="abs hero" role="img" aria-label="Warm-lit spa treatment room with two massage tables and a potted plant">
  <div class="brand-name">Amber Crest<br><span style="font-size:8px;font-weight:600">HEALTH &amp; WELLNESS GROUP</span></div>
  <nav class="main-nav">
    <a>Home</a><a>About preview</a><a>Who We Serve</a><a>Services preview</a><a>Mission &amp; Vision</a><a>Community partners</a>
  </nav>
  <a class="btn" style="left:986px;top:44px;width:138px;height:40px">Contact Us</a>
  <div class="abs nav-rule"></div>
  <h1>Helping Those Who Help Others</h1>
  <p class="lede">Providing compassionate care and wellness solutions for first responders, healthcare professionals, and our community.</p>
  <a class="btn" style="left:506px;top:332px;width:186px;height:40px">Book an Appointment</a>
  <svg class="slide-arrow" style="left:76px" width="50" height="24" viewBox="0 0 50 24"><path d="M49 12H2M12 2L2 12l10 10" fill="none" stroke="#fff" stroke-width="2"/></svg>
  <svg class="slide-arrow" style="left:1074px" width="50" height="24" viewBox="0 0 50 24"><path d="M1 12h47M38 2l10 10-10 10" fill="none" stroke="#fff" stroke-width="2"/></svg>
  <div class="dots"><span></span><span class="on"></span><span></span></div>
</header>

<section class="about">
  <div class="photo" style="left:0;top:1120px;width:215px;height:400px;background:radial-gradient(ellipse,#eef1f5 0%,rgba(255,255,255,0) 70%)" role="img" aria-label="Faint line drawing of leaves and stems"></div>
  <p class="eyebrow" style="left:146px;top:853px">A Team Committed to Care Supporting</p>
  <h2 class="section-title" style="left:146px;top:884px">Those Who Serve Others<br>With Compassion &amp; Expertise</h2>
  <div class="photo" style="left:241px;top:1024px;width:332px;height:425px;background:linear-gradient(135deg,#d9d4cc 0%,#a89070 55%,#5c4a3a 100%)" role="img" aria-label="Therapist taking notes while a client rests on a couch"></div>
  <div class="photo" style="left:666px;top:810px;width:388px;height:472px;background:linear-gradient(180deg,#e8e8e6 0%,#bdb8b0 55%,#7a6a58 100%)" role="img" aria-label="Counsellor in conversation with two clients seated in armchairs"></div>
  <p class="body-copy" style="left:666px;top:1312px;width:400px">Amber Crest Health &amp; Wellness Group is dedicated to supporting those who dedicate their lives to helping others. Our trauma-informed approach ensures personalized care for every client.</p>
  <a class="btn" style="left:666px;top:1387px;width:133px;height:41px">Read Our Story</a>
</section>

<section class="services">
  <p class="eyebrow" style="left:0;top:1579px;width:1200px;text-align:center">Our Services</p>
  <h2 class="section-title" style="left:0;top:1608px;width:1200px;text-align:center">Our Comprehensive Wellness Services</h2>
  <article class="service" style="left:76px"><div class="photo" style="background:linear-gradient(135deg,#e9e6e1,#5e4a6e 60%,#3b3a3a)" role="img" aria-label="Therapist speaking with a client and his dog"></div><h3>Mental Health Therapy</h3></article>
  <article class="service" style="left:340px"><div class="photo" style="background:linear-gradient(135deg,#f1e7e0,#d9b49c 55%,#f4efea)" role="img" aria-label="Woman receiving a salt scrub treatment"></div><h3>Salt Therapy</h3></article>
  <article class="service" style="left:606px"><div class="photo" style="background:radial-gradient(ellipse at 40% 30%,#ff8a6e,#d23a2e 50%,#6d1d1b)" role="img" aria-label="Client resting under a red-light therapy panel"></div><h3>Red-Light Therapy</h3></article>
  <article class="service" style="left:872px"><div class="photo" style="background:linear-gradient(135deg,#d8e4ee,#b9c9d6 50%,#f2f4f6)" role="img" aria-label="Clinician fitting a neurofeedback headset on a patient"></div><h3>Neurofeedback</h3></article>
  <svg class="abs" style="left:554px;top:1999px" width="40" height="20" viewBox="0 0 40 20"><path d="M39 10H2M10 2L2 10l8 8" fill="none" stroke="#1d1d1f" stroke-width="1.8"/></svg>
  <svg class="abs" style="left:604px;top:1999px" width="40" height="20" viewBox="0 0 40 20"><path d="M1 10h37M30 2l8 8-8 8" fill="none" stroke="#27598f" stroke-width="1.8"/></svg>
</section>

<section class="abs video" role="img" aria-label="Row of blue cushioned relaxation loungers on a wooden floor">
  <div class="play" style="top:147px">Play Now</div>
</section>

<section class="audiences">
  <h2 class="section-title" style="left:0;top:2676px;width:1200px;text-align:center">Supporting Heroes &amp; Community Members</h2>
  <div class="audience" style="left:104px"><div class="icon"><svg width="34" height="26" viewBox="0 0 34 26" fill="none" stroke="#fff" stroke-width="1.8"><rect x="2" y="4" width="19" height="15"/><path d="M21 9h6l5 5v5H21z"/><circle cx="9" cy="21" r="3"/><circle cx="26" cy="21" r="3"/><path d="M11.5 8v7M8 11.5h7"/></svg></div><p>First Responders &amp; Emergency Personnel.</p></div>
  <div class="v-rule" style="left:432px"></div>
  <div class="audience" style="left:440px"><div class="icon"><svg width="32" height="32" viewBox="0 0 32 32" fill="none" stroke="#fff" stroke-width="1.8"><circle cx="16" cy="16" r="13"/><path d="M16 9v14M9 16h14"/></svg></div><p>Healthcare Professionals.</p></div>
  <div class="v-rule" style="left:768px"></div>
  <div class="audience" style="left:774px"><div class="icon"><svg width="32" height="32" viewBox="0 0 32 32" fill="none" stroke="#fff" stroke-width="1.8"><circle cx="16" cy="16" r="13"/><circle cx="16" cy="16" r="8"/><path d="M16 12c-3 2-3 6 0 8 3-2 3-6 0-8z"/></svg></div><p>Individuals seeking holistic wellness...</p></div>
</section>

<section class="mission">
  <div class="photo" style="left:111px;top:2976px;width:263px;height:314px;background:linear-gradient(160deg,#eceae6,#c9c4bc 50%,#1e3a66 100%)" role="img" aria-label="Man in a white sweater seated in a blue armchair"></div>
  <div class="photo" style="left:396px;top:3017px;width:263px;height:314px;background:linear-gradient(160deg,#efe9e2,#c7b59f 55%,#7a6552)" role="img" aria-label="Small group support session seated in a circle"></div>
  <h2 class="section-title" style="left:714px;top:3060px">Our Mission &amp; Vision</h2>
  <p class="body-copy" style="left:714px;top:3117px;width:380px">Our mission is to provide compassionate, evidence-based wellness care to those who serve others. We envision a community where first responders and healthcare professionals receive the support they need to thrive.</p>
  <a class="btn" style="left:714px;top:3210px;width:220px;height:40px">Learn More About Our Mission</a>
</section>

<footer class="abs cta-band"></footer>
<h2 class="abs" style="left:0;top:3522px;width:1200px;text-align:center;color:#fff;font-size:52px;font-weight:600;letter-spacing:-1.5px">Start Your Wellness Journey Today</h2>
<a class="btn btn-light" style="left:446px;top:3606px;width:190px;height:40px">Schedule an Appointment</a>
<a class="btn btn-outline" style="left:643px;top:3606px;width:111px;height:40px">Contact Us</a>
<div class="abs foot-rule" style="top:3692px"></div>
<div class="brand-name" style="left:500px;top:3780px;width:200px;font-size:24px">Amber Crest<br><span style="font-size:9px">HEALTH &amp; WELLNESS GROUP</span></div>
<nav class="footer-nav"><a>Home</a><a>About preview</a><a>Who We Serve</a><a>Services preview</a><a>Mission &amp; Vision</a><a>Community partners</a></nav>
<div class="social"><span></span><span class="dim"></span><span class="dim"></span><span class="dim"></span></div>
<div class="abs foot-rule" style="top:4024px"></div>
<p class="copyright">© 2026 Amber Crest Health &amp; Wellness Group. All Rights Reserved.</p>
<a class="to-top" aria-label="Back to top"><svg width="14" height="9" viewBox="0 0 14 9"><path d="M1 1l6 6 6-6" fill="none" stroke="#27598f" stroke-width="2"/></svg></a>

</body>
</html>
```